Providing Back Office Solutions to Financial Advisors and Attorney Needs a Business Card Design

Need a Business Card Design that speaks to Financial Advisor and Attorneys. Some of the word that come to mind is Clean/Simple & Futuristic.

Industry/Entity Type

Business

```html
<!DOCTYPE html>
<html lang="en">
<head>
<meta charset="utf-8">
<title>Lumora Business Card</title>
<link rel="stylesheet" href="https://fonts.googleapis.com/css2?family=Arimo:wght@400;700&family=Tinos&display=swap">
<style>
  :root {
    --backdrop: #e9e7e4;
    --card: #ffffff;
    --brand-blue: #0b7fc4;
    --name-blue: #1a6fb3;
    --ink: #111111;
  }
  html, body {
    margin: 0;
    width: 1200px;
    height: 900px;
    overflow: hidden;
    background: var(--backdrop);
  }
  .canvas {
    position: relative;
    width: 1200px;
    height: 900px;
  }
  .card {
    position: absolute;
    left: 100px;
    top: 165px;
    width: 1000px;
    height: 570px;
    background: var(--card);
    box-shadow: 0 8px 24px rgba(0, 0, 0, 0.12);
  }
  .accent-bar {
    position: absolute;
    left: 0;
    top: 228px;
    width: 34px;
    height: 302px;
    background: var(--brand-blue);
    border-radius: 0 6px 6px 0;
  }
  .identity {
    position: absolute;
    left: 64px;
    top: 226px;
  }
  .person-name {
    margin: 0;
    font-family: "Tinos", "Times New Roman", serif;
    font-weight: 400;
    font-size: 46px;
    line-height: 1;
    color: var(--name-blue);
  }
  .person-title {
    margin: 2px 0 0;
    font-family: "Arimo", Arial, sans-serif;
    font-size: 26px;
    line-height: 1.1;
    color: var(--ink);
  }
  .contact-list {
    position: absolute;
    left: 50px;
    top: 348px;
    margin: 0;
    padding: 0;
    list-style: none;
    font-family: "Arimo", Arial, sans-serif;
    font-size: 29px;
    line-height: 1;
    color: var(--ink);
  }
  .brand {
    position: absolute;
    right: 40px;
    top: 58px;
    display: flex;
    align-items: center;
    gap: 14px;
  }
  .brand-square {
    width: 58px;
    height: 58px;
    background: var(--brand-blue);
  }
  .brand-name {
    font-family: "Arimo", Arial, sans-serif;
    font-weight: 700;
    font-size: 54px;
    letter-spacing: 2px;
    color: var(--brand-blue);
  }
</style>
</head>
<body>
  <main class="canvas">
    <section class="card" aria-label="Business card front">
      <div class="brand">
        <span class="brand-square" aria-hidden="true"></span>
        <span class="brand-name">LUMORA</span>
      </div>

      <div class="accent-bar" aria-hidden="true"></div>

      <div class="identity">
        <h1 class="person-name">Jane Doe</h1>
        <p class="person-title">Chief Executive Officer</p>
      </div>

      <ul class="contact-list">
        <li>Suite 5, 89 Sample Street</li>
        <li>Phone: 123 456 789</li>
        <li>Cell: 1234 567 89</li>
        <li>Email: yourname@yourcompany.com</li>
        <li>www.yourcompany.com</li>
      </ul>
    </section>
  </main>
</body>
</html>
```